" A Vasculária é uma clínica formada por profissionais especializados e em constante atualizaçao, capazes de atender as principais demandas de prevençao, diagnósticos e reabilitaçao da saúde vascular. Destaca-se por cuidar de pessoas e nao apenas tratar doenças. "

```html
<!DOCTYPE html>
<html lang="pt-BR">
<head>
<meta charset="utf-8">
<title>Vasculária — Receituário</title>
<link rel="stylesheet" href="https://fonts.googleapis.com/css2?family=Open+Sans:wght@400;600;700&display=swap">
<style>
  :root {
    --board: #87888a;
    --page: #ffffff;
    --brand-blue: #2a86c4;
    --brand-blue-light: #8fc4e6;
    --brand-red: #e2323a;
    --tint: #f7dadc;
    --ink: #6b6e72;
    --label: #ffffff;
  }
  * { margin: 0; padding: 0; box-sizing: border-box; }
  html, body { width: 1200px; height: 1200px; overflow: hidden; background: #fff; }
  body { position: relative; font-family: "Open Sans", Arial, sans-serif; }
  .board {
    position: absolute; left: 0; top: 180px; width: 1200px; height: 840px;
    background: var(--board);
  }
  .board-label {
    position: absolute; left: 29px; top: 22px;
    color: var(--label); font: 400 34px/1 Arial, "Open Sans", sans-serif;
  }
  .sheet {
    position: absolute; left: 389px; top: 98px; width: 432px; height: 615px;
    background: var(--page);
    box-shadow: 4px 6px 14px rgba(0,0,0,.35);
    overflow: hidden;
  }
  .sheet-edge { position: absolute; left: 0; top: 0; width: 12px; height: 100%; }
  .brand {
    position: absolute; top: 18px; left: 0; width: 100%; text-align: center;
  }
  .brand-name {
    color: var(--brand-blue); font-weight: 700; font-size: 17px; letter-spacing: .5px;
    text-transform: uppercase;
  }
  .brand-tagline {
    color: var(--brand-blue); font-size: 6px; letter-spacing: .4px; margin-top: 1px;
  }
  .background-art {
    position: absolute; left: 12px; top: 140px; width: 420px; height: 300px;
    background: radial-gradient(ellipse 70% 45% at 60% 45%, var(--tint) 0%, rgba(247,218,220,.45) 45%, rgba(255,255,255,0) 100%);
  }
  .contact {
    position: absolute; left: 30px; bottom: 26px; list-style: none;
    color: var(--ink); font-size: 8.5px;
  }
  .contact li { display: flex; align-items: center; gap: 8px; height: 17px; }
  .contact-icon {
    width: 11px; height: 11px; border: 1px solid #a9acb0; border-radius: 2px;
    display: flex; align-items: center; justify-content: center;
  }
</style>
</head>
<body>
  <section class="board">
    <h1 class="board-label">Receituário</h1>

    <article class="sheet">
      <svg class="sheet-edge" viewBox="0 0 12 615" preserveAspectRatio="none" aria-hidden="true">
        <defs>
          <linearGradient id="edgeBlue" x1="0" y1="0" x2="0" y2="1">
            <stop offset="0" stop-color="#2a86c4"/>
            <stop offset=".75" stop-color="#8fc4e6"/>
            <stop offset="1" stop-color="#dcedf8"/>
          </linearGradient>
        </defs>
        <rect x="0" y="0" width="12" height="540" fill="url(#edgeBlue)"/>
        <polygon points="0,540 12,560 12,615 0,615" fill="#e2323a"/>
      </svg>

      <header class="brand">
        <div class="brand-name">Vasculária</div>
        <div class="brand-tagline">clínica de saúde vascular</div>
      </header>

      <div class="background-art" role="img" aria-label="Faint pink decorative sweep across the page body"></div>

      <ul class="contact">
        <li>
          <span class="contact-icon">
            <svg width="7" height="7" viewBox="0 0 10 10" aria-hidden="true"><path d="M2 1 L4 1 L5 3 L4 4 C4.5 5.5 5 6 6 6 L7 5 L9 6 L9 8 C5 9 1 5 2 1 Z" fill="#8a8d91"/></svg>
          </span>
          Tel.: 000 0000 - 0000
        </li>
        <li><span class="contact-icon"></span>www.vascularia.com.br</li>
        <li><span class="contact-icon"></span>Rua das Acácias nº 1000 Centro - SP</li>
      </ul>
    </article>
  </section>
</body>
</html>
```